Optician needs artistic gift voucher/ card

We are looking to design a gift card for our optician shop but instead of going for traditional gift vouchers, we would like to go with a bit more ...

Optician

• Apart from being optician voucher, could be also linked to Greenwich - maritime, prime meridian etc

```html
<!DOCTYPE html>
<html lang="en">
<head>
<meta charset="utf-8">
<title>Clear View Gift Vouchers</title>
<link rel="stylesheet" href="https://fonts.googleapis.com/css2?family=Caveat+Brush&family=Amatic+SC:wght@700&display=swap">
<style>
  :root {
    --page-bg: #eeeff0;
    --rose: #d2527a;
    --teal: #5bbfbe;
    --white: #ffffff;
    --grey-ink: #5d6166;
    --logo-grey: #a9abad;
    --web-pink: #f2a9c6;
    --wash-pink: #c98aa6;
    --wash-blue: #9fc6d9;
    --wash-green: #3f8b6e;
    --wash-ice: #d7eef2;
    --wash-sky: #a9d6e3;
  }
  * { box-sizing: border-box; margin: 0; padding: 0; }
  html, body { width: 1197px; height: 1200px; overflow: hidden; }
  body { background: var(--page-bg); position: relative; font-family: "Caveat Brush", cursive; }

  .voucher {
    position: absolute;
    width: 892px;
    height: 456px;
    overflow: hidden;
    box-shadow: 0 3px 10px rgba(0,0,0,0.18);
  }
  .voucher--fifty { left: 148px; top: 97px; }
  .voucher--hundred { left: 152px; top: 650px; }

  .voucher__artwork { position: absolute; inset: 0; }
  .voucher--fifty .voucher__artwork {
    background:
      radial-gradient(ellipse 40% 35% at 8% 85%, var(--wash-green) 0%, transparent 100%),
      radial-gradient(ellipse 55% 45% at 65% 35%, var(--wash-pink) 0%, transparent 100%),
      linear-gradient(160deg, var(--wash-blue) 0%, #c4a3b8 45%, #b8c6d8 100%);
  }
  .voucher--hundred .voucher__artwork {
    background:
      radial-gradient(ellipse 40% 30% at 70% 20%, #8fb3df 0%, transparent 100%),
      radial-gradient(ellipse 35% 30% at 95% 10%, #e8c4d6 0%, transparent 100%),
      radial-gradient(ellipse 45% 30% at 60% 95%, #b8e3d2 0%, transparent 100%),
      linear-gradient(160deg, var(--wash-sky) 0%, var(--wash-ice) 50%, #e9f4f4 100%);
  }

  .voucher__halo {
    position: absolute;
    width: 530px; height: 530px;
    left: 15px; top: -182px;
    border-radius: 50%;
    background: rgba(255,255,255,0.62);
  }
  .voucher__soft-disc {
    position: absolute;
    width: 380px; height: 380px;
    left: 575px; top: 290px;
    border-radius: 50%;
    background: rgba(255,255,255,0.35);
  }

  .voucher__title {
    position: absolute;
    left: 112px; top: 34px;
    font-size: 54px;
    font-weight: 400;
    line-height: 1;
    color: var(--rose);
    letter-spacing: 1px;
  }
  .voucher__value {
    position: absolute;
    left: 152px; top: 92px;
    font-size: 160px;
    line-height: 1;
    color: var(--teal);
  }
  .voucher--hundred .voucher__value { left: 118px; }

  .voucher__brand {
    position: absolute;
    right: 40px; top: 302px;
    display: flex; align-items: center; gap: 14px;
    font-size: 50px;
    line-height: 1;
    color: var(--white);
    letter-spacing: 2px;
  }
  .voucher--hundred .voucher__brand { color: var(--logo-grey); }
  .voucher__brand-dot {
    width: 22px; height: 22px; border-radius: 50%;
    background: currentColor;
  }

  .voucher__contact {
    position: absolute;
    left: 36px; bottom: 18px;
    font-style: normal;
    color: var(--white);
  }
  .voucher--hundred .voucher__contact { color: var(--grey-ink); }
  .voucher__address {
    font-family: "Amatic SC", sans-serif;
    font-size: 22px;
    line-height: 1.15;
    letter-spacing: 0.5px;
  }
  .voucher__web {
    font-family: "Amatic SC", sans-serif;
    font-size: 34px;
    line-height: 1.1;
    margin-top: 4px;
    letter-spacing: 1px;
    color: var(--web-pink);
  }
  .voucher--hundred .voucher__web { color: var(--grey-ink); }
</style>
</head>
<body>
  <section class="voucher voucher--fifty">
    <div class="voucher__artwork" role="img" aria-label="Watercolour artwork in pink, blue and green washes"></div>
    <div class="voucher__halo"></div>
    <div class="voucher__soft-disc"></div>
    <h2 class="voucher__title">GIFT VOUCHER</h2>
    <p class="voucher__value">£50</p>
    <div class="voucher__brand"><span class="voucher__brand-dot"></span>CLEAR VIEW</div>
    <address class="voucher__contact">
      <p class="voucher__address">24 Harbour Lane<br>Riverside, SE99 4QT</p>
      <p class="voucher__web">clearviewoptician.com</p>
    </address>
  </section>

  <section class="voucher voucher--hundred">
    <div class="voucher__artwork" role="img" aria-label="Watercolour artwork in pale icy blue and mint washes"></div>
    <div class="voucher__halo"></div>
    <div class="voucher__soft-disc"></div>
    <h2 class="voucher__title">GIFT VOUCHER</h2>
    <p class="voucher__value">£100</p>
    <div class="voucher__brand"><span class="voucher__brand-dot"></span>CLEAR VIEW</div>
    <address class="voucher__contact">
      <p class="voucher__address">24 Harbour Lane<br>Riverside, SE99 4QT</p>
      <p class="voucher__web">clearviewoptician.com</p>
    </address>
  </section>
</body>
</html>
```